BRAYLEN AT HEARTH, LLC Webpage portfolio

I want to create a Website that allows my potential clients to browse my Skilled work via before and after photos. I want the website to enhance the work that I provide and potentially drive new business, or at least solidify my work.
I also do 3D CAD and Modeling of New Spaces and it would be nice to show some of that work from pencil design to 3D modeling, which I feel may help give me more clients.

The website needs to show a solid carpenter/company with the skills to get any project completed.

Types of Jobs - Custom Carpentry & Finishes, Kitchens, Baths, Basements, Decks, Porches, Whole House Renovation - Skilled Craftsmanship (Hardwood Flooring, Floor and Wall Tile) and much more...

Target Market(s)

Residential Home Renovation, Kitchen and Bath Renovation, Home Improvement

Industry/Entity Type

Residential Construction

Number of Pages Required

5+ page

Font styles to use
Sans Serif
Script

Requirements
Must have
• Similar to Nestlyra.com, except for Braylen At Hearth.
• Must be inviting.
• My Services Offered
• A way to reach me or contact me for estimates with some sort of Screening Questionare.
Nice to have
• Inviting Colors
Should not have
• Not sure at this time

```html
<!DOCTYPE html>
<html lang="en">
<head>
<meta charset="utf-8">
<title>Braylen At Hearth — Home</title>
<link rel="stylesheet" href="https://fonts.googleapis.com/css2?family=Roboto:wght@400;500;700&display=swap">
<style>
  :root {
    --brand-blue: #1f5f86;
    --band-blue: #22658c;
    --accent-blue: #2a9fd8;
    --ink: #1d2329;
    --muted: #6b7178;
    --icon: #8a9096;
    --bar-bg: #ffffff;
    --page-bg: #f4f6f8;
    --white: #ffffff;
    --room-light: #eceae6;
    --room-mid: #d3cfc9;
    --room-warm: #a89c8f;
    --room-floor: #c4bfb8;
  }
  * { box-sizing: border-box; margin: 0; padding: 0; }
  html, body { width: 1200px; height: 676px; overflow: hidden; }
  body {
    font-family: "Roboto", Arial, sans-serif;
    background: var(--page-bg);
    color: var(--ink);
    position: relative;
  }
  .hero {
    position: absolute; left: 0; top: 0; width: 1200px; height: 482px;
    overflow: hidden;
  }
  .hero-photo {
    position: absolute; inset: 0;
    background:
      radial-gradient(ellipse 70% 45% at 42% 72%, rgba(168,156,143,0.85) 0%, rgba(168,156,143,0) 70%),
      linear-gradient(160deg, var(--room-light) 0%, var(--room-mid) 55%, var(--room-floor) 100%);
  }
  .header-shade {
    position: absolute; left: 0; top: 0; width: 1200px; height: 84px;
    background: linear-gradient(180deg, rgba(120,120,120,0.55) 0%, rgba(150,150,150,0.25) 70%, rgba(150,150,150,0) 100%);
  }
  .site-header {
    position: absolute; left: 0; top: 0; width: 1200px; height: 84px;
    display: flex; align-items: center; padding: 0 44px 0 46px;
  }
  .brand { display: flex; flex-direction: column; width: 230px; }
  .brand-row { display: flex; align-items: center; gap: 7px; }
  .brand-mark { width: 16px; height: 16px; background: var(--brand-blue); }
  .brand-name { font-weight: 700; font-size: 16px; color: var(--brand-blue); }
  .brand-tagline { font-size: 6px; color: var(--brand-blue); margin: 3px 0 0 23px; letter-spacing: 0.3px; }
  .main-nav { display: flex; gap: 36px; margin-left: 60px; }
  .main-nav a {
    color: var(--white); text-decoration: none; font-size: 14px; font-weight: 400;
    text-transform: uppercase; letter-spacing: 0.2px;
  }
  .header-actions { margin-left: auto; display: flex; gap: 6px; }
  .btn { font-size: 12px; padding: 6px 10px; border-radius: 14px; text-decoration: none; }
  .btn-outline { border: 1px solid var(--white); color: var(--white); }
  .btn-solid { background: var(--white); color: var(--ink); border: 1px solid var(--white); }
  .contact-bar {
    position: absolute; left: 0; top: 482px; width: 1200px; height: 28px;
    background: var(--bar-bg); display: flex; align-items: center; padding: 0 48px;
    font-size: 12px; color: var(--muted);
  }
  .contact-item { display: flex; align-items: center; gap: 6px; margin-right: 26px; }
  .contact-item svg { fill: var(--muted); }
  .social { margin-left: auto; display: flex; align-items: center; gap: 20px; padding-right: 16px; }
  .social-dot { width: 8px; height: 8px; border-radius: 50%; background: var(--icon); }
  .welcome {
    position: absolute; left: 0; top: 510px; width: 1200px; height: 110px;
    background: var(--band-blue); color: var(--white); text-align: center; padding-top: 10px;
  }
  .welcome h1 { font-size: 19px; font-weight: 500; }
  .welcome .rule { width: 1080px; margin: 9px auto 13px; border-top: 1px dashed rgba(255,255,255,0.75); }
  .welcome p { font-size: 12px; line-height: 1.55; width: 1070px; margin: 0 auto; }
  .services {
    position: absolute; left: 0; top: 620px; width: 1200px; height: 56px;
    background: var(--page-bg); text-align: center; padding-top: 12px;
  }
  .services h2 { font-size: 20px; font-weight: 500; color: var(--ink); }
  .services h2 span { color: var(--accent-blue); }
  .services .rule { width: 1080px; margin: 9px auto 0; border-top: 1px dashed var(--accent-blue); }
</style>
</head>
<body>
  <section class="hero">
    <div class="hero-photo" role="img" aria-label="Photograph of a bright open-plan living room with two grey sofas, orange cushions, a patterned rug, a dining table and a white kitchen"></div>
    <div class="header-shade"></div>
    <header class="site-header">
      <div class="brand">
        <div class="brand-row">
          <span class="brand-mark"></span>
          <span class="brand-name">Braylen At Hearth</span>
        </div>
        <span class="brand-tagline">DESIGN, BUILD &amp; REMODELING CONTRACTORS</span>
      </div>
      <nav class="main-nav">
        <a href="#">Home</a>
        <a href="#">About</a>
        <a href="#">Services</a>
        <a href="#">Gallery</a>
        <a href="#">Contact</a>
      </nav>
      <div class="header-actions">
        <a class="btn btn-outline" href="#">Log In</a>
        <a class="btn btn-solid" href="#">Request a Quote</a>
      </div>
    </header>
  </section>

  <div class="contact-bar">
    <span class="contact-item">
      <svg width="11" height="11" viewBox="0 0 24 24"><path d="M6.6 10.8a15 15 0 0 0 6.6 6.6l2.2-2.2c.3-.3.7-.4 1-.2 1.1.4 2.3.6 3.6.6.6 0 1 .4 1 1V20c0 .6-.4 1-1 1A17 17 0 0 1 3 4c0-.6.4-1 1-1h3.5c.6 0 1 .4 1 1 0 1.3.2 2.5.6 3.6.1.3 0 .7-.2 1z"/></svg>
      +1 800 555 01 47
    </span>
    <span class="contact-item">
      <svg width="12" height="10" viewBox="0 0 24 18"><path d="M0 0h24v18H0z M2 2v1l10 7 10-7V2z" fill-rule="evenodd"/></svg>
      info@braylenathearth.com
    </span>
    <div class="social">
      <span class="social-dot"></span>
      <span class="social-dot"></span>
      <span class="social-dot"></span>
      <svg width="11" height="11" viewBox="0 0 24 24" fill="none" stroke="#8a9096" stroke-width="3"><circle cx="10" cy="10" r="7"/><path d="M15 15l7 7"/></svg>
    </div>
  </div>

  <section class="welcome">
    <h1>Welcome to Braylen At Hearth</h1>
    <div class="rule"></div>
    <p>Sed ut perspiciatis unde omnis iste natus error sit voluptatem accusantium doloremque laudantium, totam rem aperiam, eaque ipsa quae ab illo chomu inventore veritatis et quasi architecto<br>beatae vitae dicta sunt explicabo. Nemo enim ipsam voluptatem quia voluptas sit aspernatur aut odit aut fugit, sed quia consequun.</p>
  </section>

  <section class="services">
    <h2>Our <span>Services</span></h2>
    <div class="rule"></div>
  </section>
</body>
</html>
```